Home Security Company Business Card

Looking for a eye catching business card that is non traditional and stands out but yet still looks professional. It should include all the pertinent information such as name, title, address, telephone, e-mail, website address should definitely stand out and then finally the logo.

Target Market(s)

Residential and Commercial accounts mostly upscale accounts

Industry/Entity Type

Security

Contact Information for Business Card

Name
Title
Address
Office #
Cell #
E-mail
Website

Font styles to use
Serif
Sans Serif

Requirements
Must have
• Logo, two sided color configuration
Nice to have
• You decide
Should not have
• There really aren't any.

```html
<!DOCTYPE html>
<html lang="en">
<head>
<meta charset="utf-8">
<title>Ironvale Security Systems Inc. — Business Card</title>
<link rel="stylesheet" href="https://fonts.googleapis.com/css2?family=Cinzel:wght@500&family=PT+Sans:wght@400;700&family=Sorts+Mill+Goudy&display=swap">
<style>
  :root {
    --page-bg: #e9e6e2;
    --card-light: #f6f4f1;
    --card-mid: #ece7e2;
    --card-warm: #eedad6;
    --maroon: #6b1f24;
    --maroon-deep: #5a171c;
    --gold: #c49a45;
    --icon-orange: #e3a55a;
    --ink: #6a2a2c;
  }
  html, body {
    margin: 0;
    width: 1200px;
    height: 970px;
    overflow: hidden;
    background: var(--page-bg);
  }
  .card {
    position: absolute;
    left: 60px;
    top: 178px;
    width: 1080px;
    height: 613px;
    background:
      radial-gradient(ellipse 320px 120px at 300px 500px, rgba(214,150,150,0.35), transparent 70%),
      radial-gradient(ellipse 380px 260px at 780px 220px, rgba(255,255,255,0.9), transparent 70%),
      linear-gradient(160deg, var(--card-light) 0%, var(--card-mid) 60%, var(--card-warm) 100%);
    border: 1px solid rgba(255,255,255,0.8);
    box-shadow: 0 10px 30px rgba(0,0,0,0.12);
    overflow: hidden;
  }
  .brand-band {
    position: absolute;
    left: 0; top: 0;
    width: 135px; height: 100%;
    background: linear-gradient(180deg, var(--maroon) 0%, var(--maroon-deep) 100%);
  }
  .brand-mark {
    position: absolute;
    left: 150px; top: 110px;
    width: 70px; height: 70px;
    background: var(--gold);
  }
  .company {
    position: absolute;
    left: 260px; top: 108px;
    margin: 0;
    font-family: "Cinzel", serif;
    font-weight: 500;
    color: var(--maroon);
    line-height: 1;
  }
  .company-name { display: block; font-size: 84px; letter-spacing: -1px; }
  .company-line { display: block; font-size: 36px; margin-top: 6px; letter-spacing: -0.5px; }
  .person {
    position: absolute;
    left: 260px; top: 326px;
  }
  .person-name {
    margin: 0;
    font-family: "PT Sans", sans-serif;
    font-weight: 700;
    font-size: 38px;
    color: var(--maroon);
    line-height: 1;
  }
  .person-title {
    margin: 4px 0 0;
    font-family: "PT Sans", sans-serif;
    font-size: 26px;
    color: var(--gold);
    letter-spacing: 1px;
    line-height: 1;
  }
  .contacts {
    position: absolute;
    left: 260px; top: 420px;
    margin: 0; padding: 0;
    list-style: none;
    font-family: "Sorts Mill Goudy", serif;
    font-size: 30px;
    color: var(--ink);
  }
  .contacts li {
    display: flex;
    align-items: center;
    height: 38px;
  }
  .contact-icon {
    width: 26px; height: 26px;
    margin-right: 20px;
    flex: none;
  }
  .contacts .address { margin-top: 2px; }
</style>
</head>
<body>
  <main class="card">
    <div class="brand-band"></div>
    <div class="brand-mark"></div>

    <h1 class="company">
      <span class="company-name">IRONVALE</span>
      <span class="company-line">SECURITY SYSTEMS INC.</span>
    </h1>

    <section class="person">
      <p class="person-name">Marcus Dell</p>
      <p class="person-title">Owner</p>
    </section>

    <ul class="contacts">
      <li>
        <svg class="contact-icon" viewBox="0 0 26 26" aria-hidden="true">
          <rect width="26" height="26" fill="var(--icon-orange)"/>
          <path d="M6 9 q7-5 14 0 l-2 3 h-2 l-1-2 h-4 l-1 2 h-2z M8 13 h10 l1 6 h-12z" fill="#fff"/>
        </svg>
        555-014-2280
      </li>
      <li>
        <svg class="contact-icon" viewBox="0 0 26 26" aria-hidden="true">
          <rect width="26" height="26" fill="var(--icon-orange)"/>
          <rect x="8" y="4" width="10" height="18" rx="2" fill="#fff"/>
          <rect x="10" y="7" width="6" height="10" fill="var(--icon-orange)"/>
        </svg>
        +1 555-014-2280
      </li>
      <li>
        <svg class="contact-icon" viewBox="0 0 26 26" aria-hidden="true">
          <rect width="26" height="26" fill="var(--icon-orange)"/>
          <rect x="5" y="8" width="16" height="11" fill="none" stroke="#fff" stroke-width="1.6"/>
          <path d="M5 8 l8 6 l8-6" fill="none" stroke="#fff" stroke-width="1.6"/>
        </svg>
        info@ironvaleus.com
      </li>
      <li class="address">PO Box your address 2nd Lane, USA</li>
    </ul>
  </main>
</body>
</html>
```